Most captivating card ever!

Life Coach - Professional Adventurer - Entrepreneur
I need the worlds most amazing business card for my personal brand. This business card will mostly be used to give to prospective clients for life coaching and business coaching.
Be creative, be adventurous. It needs to stand out. Make people say.. I need this guy!
My background is as an entrepreneur and professional adventurer undertaking extreme expeditions. I am now moving into life coaching.
No specific design ideas, so you have full creativity. Show me your best.
Industry/Entity Type
Life Coaching
Contact Information for Business Card
Dan Pellow
itsdanp.com.au
0468215903
Colors
Designer to choose colors to be used in the design.
Look and feel

```html
<!DOCTYPE html>
<html lang="en">
<head>
<meta charset="utf-8">
<title>Dan Pellow – Business Card</title>
<link href="https://fonts.googleapis.com/css2?family=Open+Sans:wght@300;400;600;700;800&display=swap" rel="stylesheet">
<style>
  :root {
    --page-bg: #d9dadc;
    --card-light: #f3f3f4;
    --card-mid: #dcdcdf;
    --card-shade: #c6c6ca;
    --silver-1: #efe9dc;
    --silver-2: #8d8a82;
    --ink: #2b2b2e;
    --ink-soft: #4a4a50;
    --accent: #2f8fd0;
    --white: #ffffff;
  }
  * { margin: 0; padding: 0; box-sizing: border-box; }
  html, body { width: 1200px; height: 1200px; overflow: hidden; }
  body {
    background: var(--page-bg);
    font-family: "Open Sans", Arial, sans-serif;
    display: flex;
    flex-direction: column;
    align-items: center;
    justify-content: center;
    gap: 40px;
  }
  .card {
    position: relative;
    width: 880px;
    height: 538px;
    overflow: hidden;
    box-shadow: 0 6px 18px rgba(0,0,0,0.18);
    background: var(--card-light);
  }
  .card-art { position: absolute; inset: 0; width: 100%; height: 100%; }

  /* Info side */
  .identity { position: absolute; left: 150px; top: 112px; color: var(--ink); }
  .identity-name { font-size: 30px; font-weight: 400; letter-spacing: 0.2px; }
  .identity-name strong { font-weight: 800; }
  .identity-role { font-size: 15px; letter-spacing: 1.5px; margin-left: 22px; color: var(--ink-soft); }

  .brand-mark {
    position: absolute; right: 110px; top: 160px;
    display: flex; align-items: center; gap: 12px;
    font-size: 22px; font-weight: 600; color: var(--accent);
    letter-spacing: 0.5px;
  }
  .brand-mark .dot { width: 18px; height: 18px; border-radius: 50%; background: var(--accent); }

  .contact { position: absolute; right: 70px; top: 292px; color: var(--ink); }
  .contact-row { display: flex; align-items: center; justify-content: flex-end; gap: 22px; height: 34px; }
  .contact-text { font-size: 19px; letter-spacing: 0.6px; }
  .contact-text b { font-weight: 700; }
  .contact-icon { width: 24px; height: 24px; }

  .tagline {
    position: absolute; right: 44px; bottom: 52px;
    font-size: 17px; letter-spacing: 1px; color: var(--ink);
  }

  /* Feature side */
  .feature-title {
    position: absolute; left: 316px; top: 150px; color: var(--white);
    text-shadow: 0 2px 6px rgba(0,0,0,0.35);
  }
  .feature-first { font-size: 46px; font-weight: 300; line-height: 1; letter-spacing: 1px; }
  .feature-last { font-size: 48px; font-weight: 800; line-height: 1.05; letter-spacing: 1px; }
  .feature-url { margin-top: 20px; font-size: 25px; font-weight: 400; }
  .feature-url b { font-weight: 700; }
</style>
</head>
<body>

  <!-- Info side -->
  <section class="card card-info">
    <svg class="card-art" viewBox="0 0 880 538" aria-hidden="true">
      <defs>
        <linearGradient id="infoBg" x1="0" y1="0" x2="1" y2="1">
          <stop offset="0" stop-color="#e6e6e8"/>
          <stop offset="0.5" stop-color="#f6f6f7"/>
          <stop offset="1" stop-color="#dedee1"/>
        </linearGradient>
        <linearGradient id="silver" x1="0" y1="0" x2="1" y2="1">
          <stop offset="0" stop-color="var(--silver-2)"/>
          <stop offset="0.45" stop-color="var(--silver-1)"/>
          <stop offset="1" stop-color="var(--silver-2)"/>
        </linearGradient>
        <linearGradient id="foldShade" x1="0" y1="0" x2="1" y2="0">
          <stop offset="0" stop-color="#d2d2d6"/>
          <stop offset="1" stop-color="#ececee"/>
        </linearGradient>
      </defs>
      <rect width="880" height="538" fill="url(#infoBg)"/>
      <polygon points="0,0 420,0 200,538 0,538" fill="url(#foldShade)" opacity="0.55"/>
      <polygon points="120,62 400,40 404,48 126,70" fill="url(#silver)"/>
      <polygon points="400,48 414,48 212,538 194,538" fill="url(#silver)"/>
      <polygon points="40,170 50,168 140,538 128,538" fill="url(#silver)" opacity="0.9"/>
    </svg>

    <div class="identity">
      <div class="identity-name"><strong>Dan</strong> Pellow</div>
      <div class="identity-role">LIFE COACH</div>
    </div>

    <div class="brand-mark"><span class="dot"></span>Pellow Coaching</div>

    <div class="contact">
      <div class="contact-row">
        <span class="contact-text">04 <b>682 159 03</b></span>
        <svg class="contact-icon" viewBox="0 0 24 24" aria-hidden="true">
          <path d="M6.6 10.8a15 15 0 0 0 6.6 6.6l2.2-2.2c.3-.3.7-.4 1-.2 1.1.4 2.3.6 3.6.6.6 0 1 .4 1 1V20c0 .6-.4 1-1 1A17 17 0 0 1 3 4c0-.6.4-1 1-1h3.5c.6 0 1 .4 1 1 0 1.3.2 2.5.6 3.6.1.3 0 .7-.2 1z" fill="var(--ink)"/>
        </svg>
      </div>
      <div class="contact-row">
        <span class="contact-text">ITS<b>DANP</b>.COM.AU</span>
        <svg class="contact-icon" viewBox="0 0 24 24" aria-hidden="true">
          <circle cx="12" cy="12" r="10" fill="none" stroke="var(--ink)" stroke-width="2"/>
          <ellipse cx="12" cy="12" rx="4" ry="10" fill="none" stroke="var(--ink)" stroke-width="1.6"/>
          <line x1="2" y1="12" x2="22" y2="12" stroke="var(--ink)" stroke-width="1.6"/>
        </svg>
      </div>
    </div>

    <div class="tagline">LIFE COACH - PROFESSIONAL ADVENTURER - ENTREPRENEUR</div>
  </section>

  <!-- Feature side -->
  <section class="card card-feature">
    <svg class="card-art" viewBox="0 0 880 538">
      <defs>
        <linearGradient id="featureBg" x1="0" y1="0" x2="1" y2="1">
          <stop offset="0" stop-color="#e9e9eb"/>
          <stop offset="1" stop-color="#d4d4d8"/>
        </linearGradient>
        <linearGradient id="scene" x1="0" y1="0" x2="1" y2="0.4">
          <stop offset="0" stop-color="#3fa9c9"/>
          <stop offset="0.25" stop-color="#c77aa8"/>
          <stop offset="0.45" stop-color="#4b5fc4"/>
          <stop offset="0.65" stop-color="#3c7f4a"/>
          <stop offset="0.8" stop-color="#a24fd0"/>
          <stop offset="1" stop-color="#2a4fd6"/>
        </linearGradient>
        <linearGradient id="leftFold" x1="0" y1="0" x2="1" y2="0">
          <stop offset="0" stop-color="#e3e3e6"/>
          <stop offset="1" stop-color="#c4c4c8"/>
        </linearGradient>
        <linearGradient id="rightFold" x1="1" y1="0" x2="0" y2="0">
          <stop offset="0" stop-color="#ececee"/>
          <stop offset="1" stop-color="#c8c8cc"/>
        </linearGradient>
      </defs>
      <rect width="880" height="538" fill="url(#featureBg)" aria-hidden="true"/>
      <polygon points="30,110 820,90 470,538" fill="url(#scene)" role="img" aria-label="Vivid painted lake and forest landscape in teal, violet and magenta"/>
      <polygon points="0,110 300,110 300,120 12,120" fill="#f4f4f5" aria-hidden="true"/>
      <polygon points="0,0 880,0 880,60 240,110 0,110" fill="#efeff1" aria-hidden="true"/>
      <polygon points="0,110 30,110 330,538 0,538" fill="url(#leftFold)" aria-hidden="true"/>
      <polygon points="30,150 60,150 360,538 250,538" fill="#ebebed" opacity="0.7" aria-hidden="true"/>
      <polygon points="820,90 880,84 880,538 470,538" fill="url(#rightFold)" aria-hidden="true"/>
      <polygon points="820,90 880,84 880,538 610,538" fill="#f1f1f3" opacity="0.7" aria-hidden="true"/>
    </svg>

    <div class="feature-title">
      <div class="feature-first">DAN</div>
      <div class="feature-last">PELLOW</div>
      <div class="feature-url"><b>itsdanp</b>.com.au</div>
    </div>
  </section>

</body>
</html>
```